China Restaurant sucht kreatives Speisekarten-Design
Zielgruppe
Wir sind ein China Restaurant und sind auf der Suche nach der perfekten Speisekarte. Unsere Zielgruppe sind Familien sowie ältere Kundschaften.
Aufgabenstellung
Die Speisekarte soll in einem Asiatischen Stil designt werden, der Designer kann seine Kreativität frei lauf lassen. Wir benötigen DIN 4 Format.

```html
<!DOCTYPE html>
<html lang="de">
<head>
<meta charset="utf-8">
<title>China-Restaurant LOTUS – Speisekarte</title>
<link href="https://fonts.googleapis.com/css2?family=Alegreya:wght@400;500&family=Alegreya+Sans:wght@400;500&family=Kaushan+Script&display=swap" rel="stylesheet">
<style>
  :root{
    --backdrop:#efe9e2;
    --red-top:#d2171c;
    --red-mid:#b3150f;
    --red-bottom:#6c1604;
    --gold:#d9b56a;
    --white:#ffffff;
    --photo-dark:#3a1a0c;
    --photo-warm:#b8894a;
    --pagoda:rgba(90,14,4,0.45);
  }
  *{margin:0;padding:0;box-sizing:border-box}
  html,body{width:1200px;height:800px;overflow:hidden;background:var(--backdrop)}
  .menu-set{position:relative;width:1200px;height:800px}
  .page{
    position:absolute;top:137px;width:372px;height:525px;overflow:hidden;
    background:linear-gradient(180deg,var(--red-top) 0%,var(--red-mid) 45%,var(--red-bottom) 80%,var(--red-bottom) 100%);
    box-shadow:0 3px 10px rgba(0,0,0,.25);
  }
  .page--cover{left:28px}
  .page--drinks{left:414px}
  .page--back{left:800px}
  .frame{position:absolute;inset:0}
  .pagoda{
    position:absolute;left:80px;top:280px;width:212px;height:110px;
    background:radial-gradient(ellipse at 50% 60%,var(--pagoda) 0%,rgba(90,14,4,.25) 55%,transparent 75%);
  }
  .cover-photo{
    position:absolute;left:88px;top:37px;width:193px;height:108px;
    background:linear-gradient(160deg,var(--photo-dark) 0%,#5a2c12 40%,var(--photo-warm) 100%);
    box-shadow:-6px 5px 8px rgba(0,0,0,.35);
  }
  .centered{position:absolute;left:0;right:0;text-align:center}
  .serif-gold{font-family:'Alegreya',serif;color:var(--gold);font-size:20px;font-weight:400;line-height:1}
  .brand-name{font-family:'Alegreya Sans',sans-serif;color:var(--white);font-size:31px;font-weight:500;letter-spacing:1px;line-height:1}
  .welcome-script{font-family:'Kaushan Script',cursive;color:var(--gold);font-size:17px;line-height:28px}
  .drinks-title{top:29px;font-size:20px}
  .section{position:absolute;left:79px;width:210px}
  .section-title{font-family:'Kaushan Script',cursive;color:var(--white);font-size:9.5px;font-weight:400;line-height:12px;margin-bottom:2px}
  .row{display:grid;grid-template-columns:144px 25px 25px;font-family:'Alegreya Sans',sans-serif;color:var(--white);font-size:7px;line-height:9px;padding-left:4px}
  .row span:nth-child(3){text-align:right}
  .row--gap{height:9px}
  .contact{font-family:'Alegreya',serif;color:var(--gold);font-size:6px;line-height:10px}
</style>
</head>
<body>
<div class="menu-set">

  <section class="page page--cover">
    <svg class="frame" width="372" height="525" viewBox="0 0 372 525" fill="none" stroke="var(--gold)" stroke-width="1.6">
      <polyline points="18,157 18,18 119,18"/><polyline points="26,70 26,26 60,26"/>
      <polyline points="354,157 354,18 253,18"/><polyline points="346,70 346,26 312,26"/>
      <polyline points="18,369 18,508 119,508"/><polyline points="26,456 26,500 60,500"/>
      <polyline points="354,369 354,508 253,508"/><polyline points="346,456 346,500 312,500"/>
    </svg>
    <div class="cover-photo" role="img" aria-label="Foto des Gastraums mit gedeckten runden Tischen"></div>
    <div class="pagoda" role="img" aria-label="Schattenbild einer Pagode"></div>
    <p class="centered serif-gold" style="top:178px">Herzlich Willkommen im</p>
    <p class="centered serif-gold" style="top:207px">China-Restaurant</p>
    <p class="centered brand-name" style="top:240px">LOTUS</p>
    <p class="centered welcome-script" style="top:415px">Wir wünschen Ihnen<br>einen angenehmen Aufenthalt!</p>
  </section>

  <section class="page page--drinks">
    <svg class="frame" width="372" height="525" viewBox="0 0 372 525" fill="none" stroke="var(--gold)" stroke-width="1.6">
      <polyline points="18,157 18,18 119,18"/><polyline points="26,70 26,26 60,26"/>
      <polyline points="354,157 354,18 253,18"/><polyline points="346,70 346,26 312,26"/>
      <polyline points="18,369 18,508 119,508"/><polyline points="26,456 26,500 60,500"/>
      <polyline points="354,369 354,508 253,508"/><polyline points="346,456 346,500 312,500"/>
    </svg>
    <div class="pagoda" role="img" aria-label="Schattenbild einer Pagode"></div>
    <h1 class="centered serif-gold drinks-title">Getränke</h1>

    <div class="section" style="top:80px">
      <h2 class="section-title">Alkoholfreie Getränke</h2>
      <div class="row"><span></span><span>klein</span><span>groß</span></div>
      <div class="row"><span>Cola/ Orangenlimo/ Kräuterlimo/ Zitronenlimo</span><span>2,10</span><span>3,40</span></div>
      <div class="row"><span>Cola-Mix</span><span>2,20</span><span>3,50</span></div>
      <div class="row"><span>Eistee</span><span>2,10</span><span>3,00</span></div>
      <div class="row"><span>Soda</span><span>1,80</span><span>2,50</span></div>
      <div class="row"><span>Mineralwasser mit/ohne</span><span>2,10</span><span></span></div>
      <div class="row"><span>Apfel-, Orangen-, Johannisbeersaft</span><span>2,20</span><span>3,60</span></div>
      <div class="row"><span>Bitter Lemon</span><span>2,30</span><span>3,60</span></div>
      <div class="row"><span>Mangosaft/ Lycheesaft</span><span>2,50</span><span></span></div>
    </div>

    <div class="section" style="top:191px">
      <h2 class="section-title">Flaschenweine</h2>
      <div class="row row--gap"></div>
      <div class="row"><span>Weiß</span><span></span><span></span></div>
      <div class="row"><span>Grüner Veltliner</span><span>14,50</span><span></span></div>
      <div class="row"><span>Welschriesling</span><span>14,50</span><span></span></div>
      <div class="row row--gap"></div>
      <div class="row"><span>Rot</span><span></span><span></span></div>
      <div class="row"><span>Beaujolais</span><span>19,40</span><span></span></div>
      <div class="row"><span>Blaufränkisch</span><span>14,50</span><span></span></div>
    </div>

    <div class="section" style="top:292px">
      <h2 class="section-title">Alkoholische Getränke</h2>
      <div class="row"><span></span><span>klein</span><span>groß</span></div>
      <div class="row"><span>Hausbier vom Fass</span><span>3,00</span><span>3,60</span></div>
      <div class="row"><span>Radler</span><span>3,20</span><span>3,80</span></div>
      <div class="row"><span>Chinesisches Bier</span><span>3,60</span><span></span></div>
      <div class="row"><span>Weißbier hell/ dunkel</span><span>3,60</span><span></span></div>
      <div class="row"><span>alkoholfreies Bier</span><span>3.60</span><span></span></div>
    </div>

    <div class="section" style="top:374px">
      <h2 class="section-title">offene Weine</h2>
      <div class="row"><span></span><span>1/8</span><span>1/4</span></div>
      <div class="row"><span>Weißwein</span><span>2,10</span><span>3,00</span></div>
      <div class="row"><span>Rotwein</span><span>2.10</span><span>3,00</span></div>
      <div class="row"><span>weißer Spritzer</span><span>2,50</span><span></span></div>
      <div class="row"><span>süßer Spritzer</span><span>2,70</span><span></span></div>
      <div class="row"><span>roter Spritzer</span><span>2,50</span><span></span></div>
      <div class="row"><span>süßer roter Spritzer</span><span>2,80</span><span></span></div>
      <div class="row"><span>Lambrusco</span><span>2,30</span><span>3,90</span></div>
      <div class="row"><span>Rosewein</span><span>2,10</span><span>3,00</span></div>
    </div>
  </section>

  <section class="page page--back">
    <svg class="frame" width="372" height="525" viewBox="0 0 372 525" fill="none" stroke="var(--gold)" stroke-width="1.6">
      <polyline points="18,157 18,18 119,18"/><polyline points="26,70 26,26 60,26"/>
      <polyline points="354,157 354,18 253,18"/><polyline points="346,70 346,26 312,26"/>
      <polyline points="18,369 18,508 119,508"/><polyline points="26,456 26,500 60,500"/>
      <polyline points="354,369 354,508 253,508"/><polyline points="346,456 346,500 312,500"/>
    </svg>
    <div class="pagoda" role="img" aria-label="Schattenbild einer Pagode"></div>
    <p class="centered serif-gold" style="top:395px">China-Restaurant</p>
    <p class="centered brand-name" style="top:428px">LOTUS</p>
    <p class="centered contact" style="top:462px">Musterstraße 1 · 12345 Musterstadt</p>
    <p class="centered contact" style="top:472px">Telefon :</p>
    <p class="centered contact" style="top:487px">www.lotus-musterstadt.de</p>
  </section>

</div>
</body>
</html>
```